Improving a camping website homepage header*

My client is very happy with his new website and its new functionalities. However, he's not very happy about the homepage design. Specifically, the header(this includes the menu, large header image and two columns beneath that). You can find the website here: http://linkhop.example/tentsiteDemo .

He forwarded me several other websites he likes. Which can be found in the attachments. I also included several pictures of the camping.

I'm looking for a design that will improve the header of the homepage with room for other global style chances. The logo cannot be changed.

Attachments
1) His old website homepage
2) Website mockup he liked.
3) Another website mockup he liked.

Other images can be found on the new website http://linkhop.example/tentsiteDemo or his old website http://linkhop.example/priorTentsiteDemo.

Can you help us?
Updates

Hello guys. Here's a bit more information - Language used on the website is dutch. - The two columns left/right are supposed to link to Hire/Buy chalets. The client indicated that he finds these links important, but doesn't like the current design. I think this is partially the case because he doesn't like the icons. I'm looking forward to your designs!

Target Market(s)

30-50 year old wealthy people that want to purchase or rent cabins in the Netherlands.

Number of Pages Required

1 page

Colors

Designer to choose colors to be used in the design.

Requirements
Must have
• Improved header
Nice to have
• Global style changes
Should not have
• Logo changes

```html
<!DOCTYPE html>
<html lang="en">
<head>
<meta charset="utf-8">
<title>Parc Linderhof</title>
<link href="https://fonts.googleapis.com/css2?family=Open+Sans:wght@400;600&family=Oswald:wght@400;500&display=swap" rel="stylesheet">
<style>
:root{
  --green:#4a8c1c;
  --green-bright:#5aa624;
  --green-dark:#1f4a0c;
  --orange:#e8700f;
  --charcoal:#3c3c3c;
  --ink:#1e1e1e;
  --text:#444;
  --footer:#2b2d31;
  --footer-bottom:#35373b;
  --footer-text:#b7b9bd;
  --white:#fff;
}
*{margin:0;padding:0;box-sizing:border-box}
html,body{width:1200px;height:2490px;overflow:hidden}
body{position:relative;font-family:"Open Sans",Arial,sans-serif;color:var(--text);background:var(--white)}
.abs{position:absolute}

/* top bar */
.topbar{left:0;top:0;width:1200px;height:42px;background:var(--green)}
.topbar .phone{left:88px;top:9px;color:var(--white);font-size:19px;display:flex;align-items:center;gap:6px}
.topbar .search{left:985px;top:10px}
.topbar .login{left:1025px;top:0;width:88px;height:42px;background:var(--orange);color:var(--white);font-size:20px;display:flex;align-items:center;justify-content:center}

/* header */
.logo{left:88px;top:68px;display:flex;align-items:center;gap:12px}
.logo .mark{width:40px;height:40px;border-radius:50%;background:var(--green)}
.logo .name{font-size:26px;font-weight:600;color:var(--green)}
.nav{left:476px;top:84px;display:flex;gap:36px;font-size:17px;font-weight:600;color:var(--ink)}
.nav .active{color:var(--green-bright)}

/* hero */
.hero{left:0;top:153px;width:1200px;height:620px;background:linear-gradient(180deg,#6f7478 0%,#8e8f88 35%,#6a7050 70%,#4f6a36 100%)}
.hero-title{left:0;top:395px;width:1200px;text-align:center;font-family:"Oswald",Arial,sans-serif;font-size:64px;font-weight:500;color:var(--white)}
.hero-sub{left:0;top:475px;width:1200px;text-align:center;font-family:"Oswald",Arial,sans-serif;font-size:25px;color:var(--white)}
.hero-dots{left:1170px;top:398px;display:flex;flex-direction:column;gap:12px}
.hero-dots span{width:8px;height:8px;border-radius:50%;background:var(--white)}
.hero-dots .on{background:var(--orange)}
.hero-edge{left:0;top:700px}

/* feature cards */
.card{top:642px;width:312px;height:214px;color:var(--white);text-align:center;padding:80px 28px 0;box-shadow:0 8px 18px rgba(0,0,0,.25)}
.card h3{font-size:22px;font-weight:400;margin-bottom:12px}
.card p{font-size:13.5px;line-height:23px}
.card .icon{position:absolute;left:111px;top:-30px;width:90px;height:90px;border-radius:50%;background:var(--white);display:flex;align-items:center;justify-content:center}
.card.rent{left:88px;background:var(--green)}
.card.park{left:438px;background:var(--charcoal)}
.card.buy{left:787px;background:var(--orange)}

/* services */
.section-title{left:0;top:955px;width:1200px;text-align:center;font-size:36px;color:var(--ink)}
.service{top:1063px;width:240px}
.service .icon{width:73px;height:73px;border-radius:50%;background:var(--orange);display:flex;align-items:center;justify-content:center;margin-left:0}
.service h4{font-size:23px;font-weight:600;color:var(--ink);margin:14px 0 8px}
.service p{font-size:14px;line-height:22px}
.read-more{display:block;margin-top:14px;font-size:14px;color:var(--orange)}

/* featured chalet */
.featured{left:0;top:1394px;width:1200px;height:382px;background:linear-gradient(180deg,#21500e,#1a440a)}
.featured h2{left:86px;top:1450px;font-size:34px;font-weight:400;color:#f0b030}
.featured-meta{left:88px;top:1518px;color:var(--white);font-size:17px;line-height:33px}
.featured-meta div{display:flex;align-items:center;gap:12px}
.specs{left:697px;top:1497px;width:360px;border-collapse:collapse;color:var(--white);font-size:17px}
.specs td{height:57px;padding-left:6px;border-bottom:1px solid rgba(255,255,255,.7)}
.specs tr:last-child td{border-bottom:none}
.specs td:first-child{border-right:1px solid rgba(255,255,255,.7);width:192px}
.specs td span{display:inline-flex;align-items:center;gap:10px}
.featured-photo{left:88px;top:1624px;width:496px;height:307px;background:linear-gradient(180deg,#9fb8c8 0%,#c9cfc0 30%,#8aa35e 60%,#4f7a24 100%);border:4px solid #eef0ea;box-shadow:0 4px 14px rgba(0,0,0,.3)}
.featured-text{left:644px;top:1817px;width:466px;border-left:3px solid var(--orange);padding-left:12px;font-size:14.5px;line-height:23px;text-align:justify}
.featured-more{left:659px;top:1894px}

/* footer */
.footer-edge{left:0;top:2060px}
.footer{left:0;top:2113px;width:1200px;height:322px;background:var(--footer)}
.footer h5{font-size:14.5px;font-weight:600;color:var(--white);margin-bottom:22px}
.footer-col{top:2160px;color:var(--footer-text);font-size:12.5px}
.contact-list div{display:flex;gap:14px;margin-bottom:11px;line-height:19px}
.contact-list svg{flex:none;margin-top:3px}
.chalet-item{display:flex;gap:14px;margin-bottom:14px}
.chalet-thumb{width:103px;height:68px;border-radius:3px;background:linear-gradient(180deg,#b8c4cc,#7a8f5a 65%,#4e6b2a)}
.chalet-item .price{color:var(--orange);margin-top:8px}
.social{display:grid;grid-template-columns:repeat(6,20px);gap:30px 30px}
.social span{width:18px;height:18px;border-radius:50%;background:var(--footer-text)}
.bottom-bar{left:0;top:2435px;width:1200px;height:55px;background:var(--footer-bottom);color:var(--footer-text);font-size:12px;padding:19px 0 0 91px}
</style>
</head>
<body>

<div class="abs topbar">
  <div class="abs phone">
    <svg width="16" height="16" viewBox="0 0 24 24" fill="#fff"><path d="M6.6 10.8a15 15 0 0 0 6.6 6.6l2.2-2.2a1 1 0 0 1 1-.25 11.4 11.4 0 0 0 3.6.6 1 1 0 0 1 1 1V20a1 1 0 0 1-1 1A17 17 0 0 1 3 4a1 1 0 0 1 1-1h3.5a1 1 0 0 1 1 1c0 1.25.2 2.45.6 3.6a1 1 0 0 1-.25 1z"/></svg>
    0100 - 22 33 44
  </div>
  <svg class="abs search" width="22" height="22" viewBox="0 0 24 24" fill="none" stroke="#fff" stroke-width="3"><circle cx="10" cy="10" r="7"/><path d="M15 15l6 6"/></svg>
  <div class="abs login">Login</div>
</div>

<div class="abs logo"><span class="mark"></span><span class="name">Parc Linderhof</span></div>
<nav class="abs nav">
  <span class="active">Home</span><span>The park</span><span>Financing</span><span>Chalets</span><span>Offers</span><span>Facilities</span><span>Contact</span>
</nav>

<div class="abs hero" role="img" aria-label="Photo of a large modern chalet with wooden gables among trees and a green lawn"></div>
<div class="abs hero-title">Parc Linderhof</div>
<div class="abs hero-sub">Neque porro quisquam est dolorem</div>
<div class="abs hero-dots"><span></span><span class="on"></span><span></span><span></span><span></span></div>
<svg class="abs hero-edge" width="1200" height="80" viewBox="0 0 1200 80">
  <polygon points="0,25 420,18 420,80 0,80" fill="var(--orange)"/>
  <polygon points="780,30 1200,20 1200,80 780,80" fill="var(--green-bright)"/>
  <path d="M0,75 Q600,30 1200,75 L1200,80 L0,80 Z" fill="#fff"/>
  <path d="M0,65 Q600,15 1200,55 L1200,80 L0,80 Z" fill="#fff"/>
</svg>

<div class="abs card rent">
  <div class="icon"><svg width="44" height="44" viewBox="0 0 24 24" fill="none" stroke="#222" stroke-width="1.4"><path d="M3 11l9-7 9 7"/><path d="M5 10v10h14V10"/><rect x="10" y="14" width="4" height="6"/><rect x="7" y="12" width="2.5" height="2.5"/><rect x="14.5" y="12" width="2.5" height="2.5"/></svg></div>
  <h3>Rent a chalet</h3>
  <p>Lorem ipsum dolor sit amet, consecte-tur adipiscing elit. Aenean euismod bibendum laoreet. Proin gravida</p>
</div>
<div class="abs card park">
  <div class="icon"><svg width="44" height="44" viewBox="0 0 24 24" fill="none" stroke="#222" stroke-width="1.4"><path d="M6 4l-3 8h6z"/><path d="M6 12v8"/><circle cx="18" cy="8" r="4"/><path d="M18 12v8"/><path d="M9 16h6M10 16v4M14 16v4"/><path d="M2 20h20"/></svg></div>
  <h3>The park</h3>
  <p>Lorem ipsum dolor sit amet, consecte-tur adipiscing elit. Aenean euismod bibendum laoreet. Proin gravida</p>
</div>
<div class="abs card buy">
  <div class="icon"><svg width="44" height="44" viewBox="0 0 24 24" fill="none" stroke="#222" stroke-width="1.4"><circle cx="12" cy="12" r="10"/><circle cx="12" cy="12" r="7.5"/><path d="M15 9a3.5 3.5 0 1 0 0 6M8 11h5M8 13h5"/></svg></div>
  <h3>Buy a chalet</h3>
  <p>Lorem ipsum dolor sit amet, consecte-tur adipiscing elit. Aenean euismod bibendum laoreet. Proin gravida</p>
</div>

<h2 class="abs section-title" style="font-weight:400">Our Services</h2>

<div class="abs service" style="left:128px">
  <div class="icon"><svg width="38" height="38" viewBox="0 0 24 24" fill="none" stroke="#fff" stroke-width="1.5"><path d="M3 11l9-7 9 7"/><path d="M5 10v10h14V10"/><rect x="10" y="14" width="4" height="6"/></svg></div>
  <h4>Renting</h4>
  <p>The point of using Lorem Ipsum is that it has a more-or-less normal distribution of letters, as opposed</p>
  <span class="read-more">Read More »</span>
</div>
<div class="abs service" style="left:496px">
  <div class="icon"><svg width="38" height="38" viewBox="0 0 24 24" fill="none" stroke="#fff" stroke-width="1.5"><path d="M6 4l-3 8h6z"/><path d="M6 12v8"/><circle cx="18" cy="8" r="4"/><path d="M18 12v8"/><path d="M2 20h20"/></svg></div>
  <h4>The park</h4>
  <p>The point of using Lorem Ipsum is that it has a more-or-less normal distribution of letters, as opposed</p>
  <span class="read-more">Read More »</span>
</div>
<div class="abs service" style="left:840px">
  <div class="icon"><svg width="38" height="38" viewBox="0 0 24 24" fill="none" stroke="#fff" stroke-width="1.5"><circle cx="12" cy="12" r="9"/><circle cx="12" cy="12" r="6.5"/><path d="M15 9a3.5 3.5 0 1 0 0 6M8 11h5M8 13h5"/></svg></div>
  <h4>Buying</h4>
  <p>The point of using Lorem Ipsum is that it has a more-or-less normal distribution of letters, as opposed</p>
  <span class="read-more">Read More »</span>
</div>

<section class="abs featured"></section>
<h2 class="abs" style="left:86px;top:1450px;font-size:34px;font-weight:400;color:#f0b030">Feature chalet</h2>
<div class="abs featured-meta">
  <div><svg width="14" height="18" viewBox="0 0 24 30" fill="#fff"><path d="M12 0a10 10 0 0 0-10 10c0 8 10 20 10 20s10-12 10-20A10 10 0 0 0 12 0zm0 14a4 4 0 1 1 0-8 4 4 0 0 1 0 8z"/></svg>Lot 190</div>
  <div><span style="width:14px;display:inline-block">€</span>205,000</div>
</div>
<table class="abs specs">
  <tr><td><span><svg width="24" height="20" viewBox="0 0 24 20" fill="none" stroke="#fff" stroke-width="1.3"><path d="M2 2v16h18z"/><path d="M6 10v4h4"/></svg>130.00 m 2</span></td><td><span><svg width="24" height="18" viewBox="0 0 24 18" fill="none" stroke="#fff" stroke-width="1.3"><path d="M2 16V4M22 16v-6H2M5 10V7h6v3"/></svg>Bedrooms: 1</span></td></tr>
  <tr><td><span><svg width="24" height="20" viewBox="0 0 24 20" fill="none" stroke="#fff" stroke-width="1.3"><path d="M2 8l10-6 10 6v11H2z"/><path d="M5 11h14M5 14h14M5 17h14"/></svg>Garages: 1</span></td><td><span><svg width="24" height="20" viewBox="0 0 24 20" fill="none" stroke="#fff" stroke-width="1.3"><path d="M4 2h6v3H4zM7 5v3M2 8h20v4a5 5 0 0 1-5 5H7a5 5 0 0 1-5-5z"/></svg>Bathrooms: 1</span></td></tr>
  <tr><td><span><svg width="24" height="20" viewBox="0 0 24 20" fill="none" stroke="#fff" stroke-width="1.3"><rect x="2" y="8" width="20" height="9" rx="2"/><path d="M6 8V4h12v4M5 17v2M19 17v2"/></svg>Energy class: A</span></td><td><span><svg width="24" height="20" viewBox="0 0 24 20" fill="none" stroke="#fff" stroke-width="1.3"><rect x="4" y="2" width="16" height="16"/><path d="M4 10h16M2 18h20"/></svg>Rooms: 1</span></td></tr>
</table>
<div class="abs featured-photo" role="img" aria-label="Photo of a white mobile chalet beside a pond with green lawn and trees"></div>
<p class="abs featured-text">The point of using Lorem Ipsum is that it has a more-or-less normal distribution of letters, as opposed to using 'Content here, content here', making it look like readable English.</p>
<span class="abs read-more featured-more">Read More »</span>

<svg class="abs footer-edge" width="1200" height="54" viewBox="0 0 1200 54"><polygon points="70,54 1200,0 1200,54" fill="var(--green-bright)"/></svg>
<footer class="abs footer" role="img" aria-label="Faint photo of the park behind the footer"></footer>

<div class="abs footer-col" style="left:91px;width:300px">
  <h5>Contact</h5>
  <div class="contact-list">
    <div><svg width="12" height="13" viewBox="0 0 12 13" fill="none" stroke="#999"><rect x="1.5" y="1.5" width="9" height="10"/><path d="M4 4h1M7 4h1M4 7h1M7 7h1"/></svg><span>Beukenlaan 14b<br>1234 AB Veldstad</span></div>
    <div><svg width="12" height="12" viewBox="0 0 24 24" fill="#999"><path d="M6.6 10.8a15 15 0 0 0 6.6 6.6l2.2-2.2a1 1 0 0 1 1-.25 11.4 11.4 0 0 0 3.6.6 1 1 0 0 1 1 1V20a1 1 0 0 1-1 1A17 17 0 0 1 3 4a1 1 0 0 1 1-1h3.5a1 1 0 0 1 1 1c0 1.25.2 2.45.6 3.6a1 1 0 0 1-.25 1z"/></svg><span>0100 - 22 33 44</span></div>
    <div><svg width="12" height="12" viewBox="0 0 12 12" fill="none" stroke="#999"><rect x="1" y="4" width="10" height="5"/><path d="M3 4V1h6v3M3 9v2h6V9"/></svg><span>0100 - 22 33 45</span></div>
    <div><svg width="12" height="12" viewBox="0 0 12 12" fill="none" stroke="#999"><rect x="1" y="2.5" width="10" height="7"/><path d="M1 2.5l5 4 5-4"/></svg><span>info@parclinderhof.example</span></div>
    <div><svg width="12" height="12" viewBox="0 0 12 12" fill="none" stroke="#999"><circle cx="6" cy="6" r="4.5"/></svg><span>parcLinderhofChat</span></div>
    <div><svg width="12" height="12" viewBox="0 0 12 12" fill="none" stroke="#999"><rect x="1" y="1.5" width="10" height="7"/><path d="M4 11h4M6 8.5V11"/></svg><span>http://parc-linderhof.example</span></div>
  </div>
</div>

<div class="abs footer-col" style="left:463px;width:300px">
  <h5>New Chalets</h5>
  <div class="chalet-item"><div class="chalet-thumb" role="img" aria-label="Thumbnail photo of a chalet"></div><div><div>Lot 190</div><div class="price">€ 350 per month</div></div></div>
  <div class="chalet-item"><div class="chalet-thumb" role="img" aria-label="Thumbnail photo of a chalet"></div><div><div>Lot 233</div><div class="price">€ 205,000</div></div></div>
</div>

<div class="abs footer-col" style="left:835px;width:300px">
  <h5>Social media</h5>
  <div class="social"><span></span><span></span><span></span><span></span><span></span><span></span><span></span><span></span><span></span><span></span><span></span><span></span></div>
</div>

<div class="abs bottom-bar">Copyright 2018 | Parc Linderhof</div>

</body>
</html>
```